Website Redesign - Money is Guaranteed!

I would like a site similar to this: http://www.givewheelsforheroes.example

old site: http://www.autosforpatriots.example

Create a professional website; a car donation site seeking leads to return calls.

Please see http://www.givewheelsforheroes.example for the concept I am after.

The webpage should have a professional feel. The pages to include are 'Home', 'About us' and 'Get Started'

Industry/Entity Type

It Professional

Coding

Coded - Design and coding required

Number of Pages Required

1 page

```html
<!DOCTYPE html>
<html lang="en">
<head>
<meta charset="utf-8">
<title>Autos for Patriots – Donate Your Car</title>
<link href="https://fonts.googleapis.com/css2?family=Open+Sans:ital,wght@0,400;0,600;0,700;0,800;1,700&family=Montserrat:wght@600;700;800&display=swap" rel="stylesheet">
<style>
:root{
  --navy:#0f1e3a;
  --header:#1b2433;
  --red:#b3141c;
  --red-dark:#8e0f15;
  --blue:#2a7fc4;
  --gold:#c9a227;
  --text:#666;
  --ink:#222;
  --black:#0a0a0a;
  --white:#fff;
}
*{box-sizing:border-box;margin:0;padding:0}
html,body{width:1200px;height:2372px;overflow:hidden}
body{font-family:"Open Sans",Arial,sans-serif;color:var(--text);background:var(--white);position:relative}

/* header */
.site-header{position:absolute;top:0;left:0;width:1200px;height:32px;background:var(--header);display:flex;align-items:center;justify-content:space-between;padding:0 40px 0 24px}
.brand{display:flex;align-items:center;gap:8px;color:var(--white);font-family:"Montserrat",sans-serif;font-weight:700;font-size:13px;letter-spacing:1px}
.brand-square{width:12px;height:12px;background:var(--gold)}
.main-nav{display:flex;gap:26px}
.main-nav a{color:var(--white);text-decoration:none;font-size:11px;font-weight:700;letter-spacing:.5px}

/* hero */
.hero{position:absolute;top:32px;left:0;width:1200px;height:352px}
.hero-photo{position:absolute;inset:0;background:linear-gradient(100deg,#1a2640 0%,#3a4a66 30%,#6d2a33 55%,#9b9ea6 78%,#565b66 100%)}
.hero-copy{position:absolute;left:150px;top:78px;color:var(--white)}
.hero-copy h1{font-family:"Montserrat",sans-serif;font-size:36px;font-weight:800;line-height:1.1}
.hero-copy h2{font-family:"Montserrat",sans-serif;font-size:24px;font-weight:700;margin:6px 0 0 60px}
.hero-call{color:#e32129;font-style:italic;font-weight:700;font-size:24px;margin:40px 0 0 110px}
.hero-phone{display:inline-block;background:var(--red);color:var(--white);font-weight:700;font-size:18px;padding:10px 34px;border-radius:4px;margin:12px 0 0 118px}

.donate-form{position:absolute;left:800px;top:42px;width:300px;height:270px;background:var(--red-dark);border:3px solid var(--red);padding:16px 18px}
.donate-form h3{color:var(--white);font-family:"Montserrat",sans-serif;font-size:19px;font-weight:700;text-align:center}
.donate-form p{color:#f3c9cb;font-size:10px;text-align:center;margin:2px 0 14px}
.field-grid{display:grid;grid-template-columns:1fr 1fr;gap:8px}
.field{height:26px;background:var(--white);border-radius:2px;font-size:10px;color:#999;display:flex;align-items:center;padding-left:8px}
.form-btn{margin:16px auto 0;width:180px;height:28px;background:var(--black);color:var(--white);font-size:10px;font-weight:700;display:flex;align-items:center;justify-content:center}

/* about */
.about{position:absolute;top:384px;left:0;width:1200px;height:356px;background:#f4f4f4}
.about-card{position:absolute;left:160px;top:70px;width:380px;height:240px;border:8px solid var(--white);box-shadow:0 4px 12px rgba(0,0,0,.25);transform:rotate(-7deg);background:linear-gradient(135deg,#6fb2d8,#4d8f52 55%,#c9b46a)}
.about-copy{position:absolute;left:620px;top:44px;width:460px}
.about-copy h2{color:var(--blue);font-family:"Montserrat",sans-serif;font-size:30px;font-weight:700;margin-bottom:12px}
.about-copy p{font-size:12px;line-height:1.6;margin-bottom:12px}

/* why */
.why{position:absolute;top:740px;left:0;width:1200px;height:420px}
.why-list{position:absolute;left:130px;top:30px;width:440px}
.section-title{color:var(--blue);font-family:"Montserrat",sans-serif;font-size:24px;font-weight:700;margin-bottom:14px}
.why-item{display:flex;gap:12px;margin-bottom:12px}
.why-icon{flex:0 0 22px;height:22px;background:var(--gold);border-radius:3px;display:flex;align-items:center;justify-content:center}
.why-item h4{color:var(--blue);font-size:13px;font-weight:700}
.why-item p{font-size:10px;line-height:1.4}
.donate-today{position:absolute;left:680px;top:30px;width:400px}
.donate-today ul{list-style:none;font-size:11px;line-height:1.7;color:var(--text)}
.donate-today li::before{content:"– "}
.diamond-photo{position:absolute;left:750px;top:200px;width:170px;height:170px;transform:rotate(45deg);border:5px solid var(--gold);background:linear-gradient(135deg,#3d5f8a,#a88a58 60%,#5a4632)}

/* silhouette band */
.skyline{position:absolute;top:1160px;left:0;width:1200px;height:140px;background:linear-gradient(180deg,#fff 0%,#fff 40%,#2a2a2a 80%,var(--black) 100%)}

/* footer */
.site-footer{position:absolute;top:1300px;left:0;width:1200px;height:1072px;background:var(--black);text-align:center;color:var(--white)}
.footer-title{color:var(--gold);font-family:"Montserrat",sans-serif;font-size:28px;font-weight:700;letter-spacing:2px;margin-top:110px}
.footer-brand{display:inline-flex;align-items:center;gap:12px;margin-top:26px;font-family:"Montserrat",sans-serif;font-weight:700;font-size:22px;letter-spacing:2px}
.footer-brand .brand-square{width:18px;height:18px}
.steps{display:flex;justify-content:center;gap:150px;margin-top:110px}
.step{width:230px}
.step-icon{width:64px;height:64px;margin:0 auto;border:3px solid var(--gold);transform:rotate(45deg);display:flex;align-items:center;justify-content:center}
.step-icon svg{transform:rotate(-45deg)}
.step h4{color:var(--gold);font-family:"Montserrat",sans-serif;font-size:18px;font-weight:700;margin-top:30px}
.step p{font-size:11px;line-height:1.5;color:#ccc;margin-top:8px}
.social{display:flex;justify-content:center;gap:22px;margin-top:110px}
.social span{width:22px;height:22px;border-radius:50%;background:#777}
</style>
</head>
<body>

<header class="site-header">
  <div class="brand"><span class="brand-square"></span>AUTOS FOR PATRIOTS</div>
  <nav class="main-nav"><a href="#">HOME</a><a href="#">ABOUT</a><a href="#">FAQ</a><a href="#">DONATE</a><a href="#">GET STARTED</a></nav>
</header>

<section class="hero">
  <div class="hero-photo" role="img" aria-label="Row of donated pickup trucks and cars in front of a waving American flag, silhouette of a saluting soldier"></div>
  <div class="hero-copy">
    <h1>Donate Your Car to Veterans</h1>
    <h2>and Get a Tax Deduction</h2>
    <div class="hero-call">Call Today to Donate</div>
    <div class="hero-phone">1-800-555-0142</div>
  </div>
  <form class="donate-form">
    <h3>Fill out the form below</h3>
    <p>to instantly donate online</p>
    <div class="field-grid">
      <div class="field">First Name</div><div class="field">Last Name</div>
      <div class="field">Phone</div><div class="field">Email</div>
      <div class="field">Year</div><div class="field">Make</div>
      <div class="field">Model</div><div class="field">Zip Code</div>
    </div>
    <div class="form-btn">CLICK TO DONATE YOUR CAR</div>
  </form>
</section>

<section class="about">
  <div class="about-card" role="img" aria-label="Cartoon illustration of a tow truck carrying a donated car on a card held in hand"></div>
  <div class="about-copy">
    <h2>ABOUT</h2>
    <p>Our team turns donated vehicles into real support for veterans and their families. Every car, truck or van you give helps fund housing, job training and care programs in your community.</p>
    <p>We handle the pickup, the paperwork and the sale, so the process stays simple for you from the first call to the final receipt.</p>
    <p>Most vehicles are accepted whether they run or not. Our drivers come to your home or office at a time that works for you.</p>
    <p>Your gift is tax deductible, and we send a written receipt soon after your vehicle is sold to a new owner.</p>
  </div>
</section>

<section class="why">
  <div class="why-list">
    <h2 class="section-title">Why Donate Your Car to Us?</h2>
    <div class="why-item"><span class="why-icon"><svg width="12" height="12" viewBox="0 0 12 12"><path d="M2 6l3 3 5-6" stroke="#fff" stroke-width="2" fill="none"/></svg></span><div><h4>IRS 501(c)3 Approved</h4><p>Your gift fully qualifies as a tax deduction.</p></div></div>
    <div class="why-item"><span class="why-icon"><svg width="12" height="12" viewBox="0 0 12 12"><path d="M2 6l3 3 5-6" stroke="#fff" stroke-width="2" fill="none"/></svg></span><div><h4>Free Local Towing to You</h4><p>We will pick up your donation, running or not, at no cost to you.</p></div></div>
    <div class="why-item"><span class="why-icon"><svg width="12" height="12" viewBox="0 0 12 12"><path d="M2 6l3 3 5-6" stroke="#fff" stroke-width="2" fill="none"/></svg></span><div><h4>IRS 501(c)3 Approved</h4><p>Our nonprofit status is on file with the IRS.</p></div></div>
    <div class="why-item"><span class="why-icon"><svg width="12" height="12" viewBox="0 0 12 12"><path d="M2 6l3 3 5-6" stroke="#fff" stroke-width="2" fill="none"/></svg></span><div><h4>Income Tax Deduction</h4><p>We help you get the highest tax write-off possible.</p></div></div>
    <div class="why-item"><span class="why-icon"><svg width="12" height="12" viewBox="0 0 12 12"><path d="M2 6l3 3 5-6" stroke="#fff" stroke-width="2" fill="none"/></svg></span><div><h4>No Paperwork Hassles</h4><p>We take care of title transfer and all forms for you.</p></div></div>
    <div class="why-item"><span class="why-icon"><svg width="12" height="12" viewBox="0 0 12 12"><path d="M2 6l3 3 5-6" stroke="#fff" stroke-width="2" fill="none"/></svg></span><div><h4>Car donations help fund programs</h4><p>Proceeds support local nonprofit veteran programs.</p></div></div>
    <div class="why-item"><span class="why-icon"><svg width="12" height="12" viewBox="0 0 12 12"><path d="M2 6l3 3 5-6" stroke="#fff" stroke-width="2" fill="none"/></svg></span><div><h4>Schedule a Free Pickup</h4><p>Book a time that suits you and we will come to you.</p></div></div>
  </div>
  <div class="donate-today">
    <h2 class="section-title">Donate Your Car Today!</h2>
    <ul>
      <li>Free pickup nationwide</li>
      <li>Any vehicle, running or not</li>
      <li>Maximum tax deduction allowed</li>
      <li>Quick and easy paperwork</li>
      <li>Receipt mailed right away</li>
    </ul>
  </div>
  <div class="diamond-photo" role="img" aria-label="Photo of veterans gathered together outdoors"></div>
</section>

<div class="skyline" role="img" aria-label="Black silhouettes of cars, trucks and vans lined up along the ground"></div>

<footer class="site-footer">
  <h2 class="footer-title">GET STARTED</h2>
  <div class="footer-brand"><span class="brand-square"></span>AUTOS FOR PATRIOTS</div>
  <div class="steps">
    <div class="step">
      <div class="step-icon"><svg width="26" height="26" viewBox="0 0 24 24"><path d="M6 2h4l2 5-3 2a11 11 0 0 0 6 6l2-3 5 2v4a2 2 0 0 1-2 2A18 18 0 0 1 4 4a2 2 0 0 1 2-2z" fill="#c9a227"/></svg></div>
      <h4>TELL US</h4>
      <p>Fill out your form below or call us at<br>1-800-555-0142</p>
    </div>
    <div class="step">
      <div class="step-icon"><svg width="26" height="26" viewBox="0 0 24 24"><path d="M12 2a7 7 0 0 0-7 7c0 5 7 13 7 13s7-8 7-13a7 7 0 0 0-7-7zm0 9.5A2.5 2.5 0 1 1 12 6.5a2.5 2.5 0 0 1 0 5z" fill="#c9a227"/></svg></div>
      <h4>WE TOW IT</h4>
      <p>We will arrange a convenient time to collect your vehicle at NO cost to you.</p>
    </div>
    <div class="step">
      <div class="step-icon"><svg width="26" height="26" viewBox="0 0 24 24"><path d="M4 12l5 5L20 6" stroke="#c9a227" stroke-width="3" fill="none"/></svg></div>
      <h4>TAX WRITE-OFF</h4>
      <p>We will provide you with a receipt that can be used to declare a tax deduction.</p>
    </div>
  </div>
  <div class="social"><span></span><span></span><span></span><span></span></div>
</footer>

</body>
</html>
```